Flyer-Design für Brick and Stone Restorator
Zielgruppe
Wir sind Sydneys führender Brick and Stone Restorator.
Aufgabenstellung
Unsere neue webseite geht in ein paar tagen online und wir möchten gerne passenden zur neuen Webseite ein corporate Flyer, letztendlich soll es ein Print Version von unserer neuen Webseite sein. Sprich die wichtigsten Informationen der Webseite soll in dem Flyer enthalten sein. Letztendlich möchte ich designer keine großen einschränkungen geben, weil das ist euer job kreativ sein ;), aber der flyer sollte evtl. so aufgebaut sein das am Ende die leute entweder uns anrufen oder doch auf unsere neue Webseite gehen sprich evtl ein QR- code or what ever.
Unsere Domain ist wattleridgeworks.com.au, aber damit ihr die neue Webseite schon sehen könnt müsst ihr auf wattleridgeworks.com.au/ new, falls dieser Link nicht mehr funktionieren sollte, ist sie schon auf der richtigen domain hochgeladen.
Falls ihr irgendwelche Logos Bilder oder sonst was benötigt und diese nicht aus der Webseite entnehmen könnt, schickt einfach eine kurze Naricht, ich beantworte diese so schnell wie möglich ;)
der Flyer soll ein 6 pager sein!!
mit freundlichen Grüßen euer Wattle Ridge Works Team

```html
<!DOCTYPE html>
<html lang="en">
<head>
<meta charset="utf-8">
<title>Wattle Ridge Works – Brochure</title>
<link rel="stylesheet" href="https://fonts.googleapis.com/css2?family=Open+Sans:wght@400;600;700&display=swap">
<style>
  :root{
    --navy:#27214f;
    --navy-deep:#1f1a44;
    --gold:#d9cba6;
    --paper:#f4f4f2;
    --ink:#2b2558;
    --backdrop:#e6e6e4;
  }
  *{box-sizing:border-box;margin:0;padding:0}
  html,body{width:1200px;height:857px;overflow:hidden;background:var(--backdrop);font-family:"Open Sans",sans-serif;color:var(--ink)}
  .brochure{position:absolute;left:50px;top:40px;width:1100px;height:778px;background:var(--paper);box-shadow:0 4px 18px rgba(0,0,0,.18);overflow:hidden}
  .panel{position:absolute;top:0;height:100%;width:366.67px}
  .panel--reviews{left:0}
  .panel--contact{left:366.67px}
  .panel--cover{left:733.33px}
  .fold{position:absolute;top:0;width:1px;height:100%;background:rgba(0,0,0,.08);z-index:5}

  .band{position:absolute;left:0;width:100%;background:var(--navy)}
  .band--footer{bottom:0;height:58px}

  /* Reviews panel */
  .reviews-head{top:26px;height:140px;display:flex;align-items:flex-end;justify-content:center;padding-bottom:30px}
  .reviews-title{color:var(--gold);font-weight:600;font-size:25px;letter-spacing:.3px}
  .reviews{position:absolute;top:190px;bottom:74px;left:26px;right:26px;display:flex;flex-direction:column;justify-content:space-between}
  .review{position:relative;text-align:center;font-size:9.5px;line-height:1.42;padding:0 18px}
  .review__name{display:block;margin-top:3px;font-weight:700}
  .review__name--plain{font-weight:400}
  .quote{position:absolute;font-family:Georgia,serif;font-size:40px;line-height:1;color:var(--gold);font-weight:700}
  .quote--open{left:-8px;bottom:-18px}
  .quote--close{right:-8px;top:-12px}

  /* shared logo */
  .brand{display:flex;flex-direction:column;align-items:center;color:#fff}
  .brand__row{display:flex;align-items:center;gap:8px}
  .brand__mark{width:14px;height:14px;background:var(--gold)}
  .brand__name{font-weight:700;font-size:24px;letter-spacing:.5px;text-transform:uppercase}
  .brand__tag{margin-top:6px;font-size:9.5px;letter-spacing:2px;text-transform:uppercase}

  .photo{position:absolute;left:366.67px;top:100px;width:733.33px;height:620px;
    background:linear-gradient(180deg,#c9d1d6 0%,#b8b2ab 18%,#7a4a36 40%,#6a3b2b 65%,#4a2e24 100%)}

  /* Contact panel */
  .contact-head{top:26px;height:160px;display:flex;align-items:center;justify-content:center}
  .contact-card{position:absolute;left:36px;top:200px;width:294px;height:488px;background:rgba(255,255,255,.88);padding:22px 22px}
  .contact-card__title{text-align:center;font-size:13px;letter-spacing:1px;margin-bottom:16px}
  .contact-list{list-style:none;font-size:11.5px;line-height:1.3}
  .contact-list li{display:flex;gap:10px;align-items:flex-start;margin-bottom:7px}
  .contact-list svg{flex:none;width:14px;height:14px;fill:var(--navy)}
  .map{margin-top:14px;height:222px;background:linear-gradient(135deg,#eceeed,#dfe3e2 60%,#cfe3c8)}

  /* Cover panel */
  .cover-head{top:26px;height:76px;display:flex;align-items:center;justify-content:center}
  .cover-head .brand__name{font-size:22px}
  .headline{position:absolute;top:200px;right:26px;left:26px;color:#fff;text-transform:uppercase;text-align:right;text-shadow:0 1px 6px rgba(0,0,0,.35)}
  .headline__lead{font-size:32px;font-weight:600;letter-spacing:2px}
  .headline__lead small{font-size:16px;letter-spacing:1px}
  .headline__line{display:block;font-size:31px;font-weight:400;letter-spacing:6px;line-height:1.15}
  .partners{position:absolute;left:20px;right:20px;top:520px;height:110px;background:rgba(255,255,255,.82);display:flex;flex-wrap:wrap;align-items:center;justify-content:space-around;padding:14px 16px}
  .partner{height:22px;border-radius:3px}
  .partner--a{width:38px;background:#3b8a3e;border-radius:50%;height:30px}
  .partner--b{width:70px;background:#2aa1d8}
  .partner--c{width:60px;background:#2456a6}
  .partner--d{width:72px;background:#7b86b8}
  .partner--e{width:74px;background:#d9222a}
  .partner--f{width:68px;background:#9bbf3a}
  .cover-foot{display:flex;flex-direction:column;align-items:flex-end;justify-content:center;padding-right:24px;color:#fff;font-size:13px;line-height:1.3}
  .cover-foot svg{width:11px;height:11px;fill:#fff;vertical-align:-1px}
</style>
</head>
<body>
<main class="brochure">
  <div class="photo" role="img" aria-label="Photograph of a restored red brick heritage building with arched windows and trees"></div>

  <section class="panel panel--reviews">
    <header class="band reviews-head"><h2 class="reviews-title">What our customers say …</h2></header>
    <div class="reviews">
      <blockquote class="review">
        <span class="quote quote--close">”</span>
        Wattle Ridge Works – my experience was great. Communication was excellent – appointments were made and kept, they gave me a honest timeframe to start the job, kept their promised start date and all the tradesmen were totally professional. They obviously took pride in their work, and cleaned up well after themselves. The job looks fantastic.
        <span class="review__name review__name--plain">Jo, Elmsford</span>
        <span class="quote quote--open">“</span>
      </blockquote>
      <blockquote class="review">
        <span class="quote quote--close">”</span>
        I would like to thank you and all the team for your politeness and good work. I am so glad I was able to have it completed earlier than expected.
        <span class="review__name">Thanks again<br>Danielle, Hartwell</span>
        <span class="quote quote--open">“</span>
      </blockquote>
      <blockquote class="review">
        <span class="quote quote--close">”</span>
        Dear Wattle Ridge Works,<br>This is a sincere thank you for the work completed recently on our house in Westbury. The boys on site were always courteous, incredibly hard-working, very skilled and professional.<br>The quote was very reasonable and all work was commenced and completed on times scheduled. The site was left clean and the finished job perfect.<br>In short, we are delighted with the work completed and with all aspects of our negotiations with your company.
        <span class="review__name review__name--plain">Thank you,</span>
        <span class="review__name" style="margin-top:0">Colin Marsh &amp; Anna Pryor, Westbury</span>
        <span class="quote quote--open">“</span>
      </blockquote>
      <blockquote class="review">
        <span class="quote quote--close">”</span>
        Thank you Ted and Dean for the work on the brick and sandstone. We are very happy with it and your professionalism through all our dealings with you. It was a pleasure having you here.
        <span class="review__name">Leah and Vik Ortega, Ashdale</span>
        <span class="quote quote--open">“</span>
      </blockquote>
    </div>
    <div class="band band--footer"></div>
  </section>

  <section class="panel panel--contact">
    <header class="band contact-head">
      <div class="brand">
        <div class="brand__row"><span class="brand__mark"></span><span class="brand__name">Wattle Ridge Works</span></div>
        <span class="brand__tag">Brick and Stone Restoration</span>
      </div>
    </header>
    <div class="contact-card">
      <h3 class="contact-card__title">CONTACT US</h3>
      <ul class="contact-list">
        <li><svg viewBox="0 0 24 24"><path d="M6.6 10.8a15 15 0 0 0 6.6 6.6l2.2-2.2c.3-.3.7-.4 1-.2 1.1.4 2.3.6 3.6.6.6 0 1 .4 1 1V20c0 .6-.4 1-1 1A17 17 0 0 1 3 4c0-.6.4-1 1-1h3.5c.6 0 1 .4 1 1 0 1.3.2 2.5.6 3.6.1.3 0 .7-.2 1z"/></svg>0400 555 218</li>
        <li><svg viewBox="0 0 24 24"><path d="M12 2a10 10 0 1 0 0 20 10 10 0 0 0 0-20zm0 2.2a7.8 7.8 0 1 1 0 15.6 7.8 7.8 0 0 1 0-15.6zM11 6h2v5.6l3.6 2.1-1 1.7L11 12.7z"/></svg>Mon - Fri 9am - 5pm</li>
        <li><svg viewBox="0 0 24 24"><path d="M2 5h20v14H2zm2 2v.4l8 5 8-5V7zm0 2.7V17h16V9.7l-8 5z"/></svg>enquiries@wattleridgeworks.com.au</li>
        <li><svg viewBox="0 0 24 24"><path d="M12 2a10 10 0 1 0 0 20 10 10 0 0 0 0-20zm-1 2.1V8H7.3A8 8 0 0 1 11 4.1zm2 0A8 8 0 0 1 16.7 8H13zM4.5 10H11v4H4.5a8 8 0 0 1 0-4zm8.5 0h6.5a8 8 0 0 1 0 4H13zm-5.7 6H11v3.9A8 8 0 0 1 7.3 16zm5.7 0h3.7a8 8 0 0 1-3.7 3.9z"/></svg>www.wattleridgeworks.com.au</li>
        <li><svg viewBox="0 0 24 24"><path d="M12 2 2 9v13h20V9zm0 2.4L19.5 9 12 13.6 4.5 9zM4 11l8 5 8-5v9H4z"/></svg>PO Box 4120, Kelvin Bay NSW 2099</li>
        <li><svg viewBox="0 0 24 24"><path d="M12 2a7 7 0 0 0-7 7c0 5.2 7 13 7 13s7-7.8 7-13a7 7 0 0 0-7-7zm0 9.5a2.5 2.5 0 1 1 0-5 2.5 2.5 0 0 1 0 5z"/></svg>5 / 12 Ironbark Lane, Kelvin Bay,<br>NSW 2099, Australia</li>
      </ul>
      <div class="map" role="img" aria-label="Street map showing the workshop location"></div>
    </div>
    <div class="band band--footer"></div>
  </section>

  <section class="panel panel--cover">
    <header class="band cover-head">
      <div class="brand">
        <div class="brand__row"><span class="brand__mark"></span><span class="brand__name">Wattle Ridge Works</span></div>
        <span class="brand__tag">Brick and Stone Restoration</span>
      </div>
    </header>
    <h1 class="headline">
      <span class="headline__lead"><small>Over</small> 20 Years <small>of</small></span>
      <span class="headline__line">Professional</span>
      <span class="headline__line">Experience</span>
    </h1>
    <div class="partners" aria-label="Partner and certification badges">
      <span class="partner partner--a"></span>
      <span class="partner partner--b"></span>
      <span class="partner partner--c"></span>
      <span class="partner partner--d"></span>
      <span class="partner partner--e"></span>
      <span class="partner partner--f"></span>
    </div>
    <footer class="band band--footer cover-foot">
      <span>www.wattleridgeworks.com.au</span>
      <span>Call us at <svg viewBox="0 0 24 24"><path d="M6.6 10.8a15 15 0 0 0 6.6 6.6l2.2-2.2c.3-.3.7-.4 1-.2 1.1.4 2.3.6 3.6.6.6 0 1 .4 1 1V20c0 .6-.4 1-1 1A17 17 0 0 1 3 4c0-.6.4-1 1-1h3.5c.6 0 1 .4 1 1 0 1.3.2 2.5.6 3.6.1.3 0 .7-.2 1z"/></svg> 0400 555 218</span>
    </footer>
  </section>

  <span class="fold" style="left:366.67px"></span>
  <span class="fold" style="left:733.33px"></span>
</main>
</body>
</html>
```